Business Card Design

I want a non fussy clear design. I like Vintage, Retro writing for the main name as it will be a banner for the roof sign.
Company name, address and ph no. I would also like a unisex symbol small in the corner of the card. The colour of the card does not have to be blue. But I do want a bright clean clear card. A head sillohette small in the other corner possibly.

Industry/Entity Type

Business

Contact Information for Business Card

Zet Hair Design
318 Kellaby Road, Kellaby
Ph (09) 4162903

Requirements
Must have
• The back of the card must have appointment time, date dont worry about the location as its obviously on the front of the card

```html
<!DOCTYPE html>
<html lang="en">
<head>
<meta charset="utf-8">
<title>Zet Hair Design – Business Card</title>
<link href="https://fonts.googleapis.com/css2?family=Poiret+One&display=swap" rel="stylesheet">
<style>
  :root {
    --page-bg: #e9e6e1;
    --card-bg: #f4f5f7;
    --damask: linear-gradient(135deg, #eef0f3 0%, #f8f9fa 50%, #eceef2 100%);
    --loop-blue: #b9c8ea;
    --flourish-blue: #c7d3ef;
    --ink: #111111;
    --ink-brown: #3a2325;
    --info-band: rgba(255, 255, 255, 0.55);
    --shadow: 0 6px 14px rgba(0, 0, 0, 0.25);
  }
  * { box-sizing: border-box; margin: 0; padding: 0; }
  html, body { width: 1200px; height: 1200px; overflow: hidden; }
  body {
    background: var(--page-bg);
    font-family: "Poiret One", sans-serif;
    color: var(--ink);
    position: relative;
  }
  .card {
    position: absolute;
    left: 130px;
    width: 940px;
    height: 537px;
    background: var(--card-bg);
    box-shadow: var(--shadow);
    overflow: hidden;
  }
  .card--front { top: 50px; }
  .card--back { top: 613px; }

  .card__pattern {
    position: absolute;
    inset: 0;
    background: var(--damask);
  }
  .loop-border {
    position: absolute;
    left: 0;
    right: 0;
    height: 26px;
    background: var(--loop-blue);
    opacity: 0.55;
  }
  .loop-border--top { top: 14px; }
  .loop-border--bottom { bottom: 14px; }

  .flourish {
    position: absolute;
    left: 0;
    top: 90px;
    width: 940px;
    height: 250px;
    border-radius: 50%;
    background: radial-gradient(ellipse at center, rgba(199, 211, 239, 0.55) 0%, rgba(199, 211, 239, 0) 70%);
  }

  .brand-name {
    position: absolute;
    left: 0;
    right: 0;
    top: 150px;
    text-align: center;
    font-size: 124px;
    line-height: 1;
    letter-spacing: -2px;
    color: var(--ink);
  }

  .info-band {
    position: absolute;
    left: 0;
    right: 0;
    top: 380px;
    height: 100px;
    background: var(--info-band);
  }
  .contact {
    position: absolute;
    left: 22px;
    top: 388px;
    font-size: 34px;
    line-height: 50px;
    letter-spacing: 0.5px;
  }
  .unisex-icon {
    position: absolute;
    right: 22px;
    top: 402px;
    width: 86px;
    height: 86px;
  }

  .appointment {
    position: absolute;
    left: 340px;
    top: 230px;
    font-size: 40px;
    line-height: 54px;
    color: var(--ink-brown);
    letter-spacing: 1px;
  }
</style>
</head>
<body>

<section class="card card--front" aria-label="Business card front">
  <div class="card__pattern" role="img" aria-label="Soft white damask background pattern"></div>
  <div class="loop-border loop-border--top" role="img" aria-label="Light blue looped line border"></div>
  <div class="flourish" role="img" aria-label="Pale blue baroque scroll flourish"></div>
  <h1 class="brand-name">Zet Hair Design</h1>
  <div class="info-band"></div>
  <address class="contact" style="font-style:normal">
    <div class="contact__address">318 Kellaby Road, Kellaby</div>
    <div class="contact__phone">(09) 4162903</div>
  </address>
  <svg class="unisex-icon" viewBox="0 0 86 86" aria-label="Unisex symbol" role="img">
    <g fill="none" stroke="var(--ink)" stroke-width="6" stroke-linecap="square">
      <circle cx="34" cy="54" r="15"/>
      <circle cx="55" cy="54" r="15"/>
      <line x1="22" y1="44" x2="8" y2="30"/>
      <line x1="6" y1="42" x2="22" y2="26"/>
      <line x1="57" y1="39" x2="57" y2="8"/>
      <polyline points="47,18 57,6 67,18"/>
    </g>
  </svg>
  <div class="loop-border loop-border--bottom" role="img" aria-label="Light blue looped line border"></div>
</section>

<section class="card card--back" aria-label="Business card back">
  <div class="card__pattern" role="img" aria-label="Soft white damask background pattern"></div>
  <div class="loop-border loop-border--top" role="img" aria-label="Light blue looped line border"></div>
  <div class="appointment">
    <p class="appointment__time">Appointment time:</p>
    <p class="appointment__date">Date:</p>
  </div>
  <div class="loop-border loop-border--bottom" role="img" aria-label="Light blue looped line border"></div>
</section>

</body>
</html>
```